Brackwell HVAC Service LLC Business Card

We just got a design created by one of your designers for a logo and now would like help with a business card design. The information to be included on the card is as follows:
Brackwell HVAC Service LLC (I will attach logo design)
P.O. Box 418
Brenvale, CO 80694
(970) 555-0147
Dale Vonnholt
I might include an e-mail address, but I'm not sure yet.
Target Market(s)
Customers needing service or repairs done on their heating and air conditioning systems.
Industry/Entity Type
Business
Contact Information for Business Card
P.O. Box 418
Brenvale, CO 80694
(970) 555-0147
Dale Vonnholt

```html
<!DOCTYPE html>
<html lang="en">
<head>
<meta charset="utf-8">
<title>Brackwell HVAC Service LLC – Business Card</title>
<link rel="stylesheet" href="https://fonts.googleapis.com/css2?family=Arimo:wght@400;700&display=swap">
<style>
  :root {
    --navy: #0f2657;
    --red: #e3202b;
    --white: #ffffff;
    --sun-tone: #f27a7e;
    --card-w: 1200px;
    --card-h: 693px;
  }
  * { margin: 0; padding: 0; box-sizing: border-box; }
  html, body {
    width: var(--card-w);
    height: var(--card-h);
    overflow: hidden;
    background: var(--white);
  }
  .card {
    position: relative;
    width: var(--card-w);
    height: var(--card-h);
    overflow: hidden;
    background: var(--white);
    font-family: "Arimo", Arial, sans-serif;
  }
  .card-backdrop {
    position: absolute;
    inset: 0;
    width: 100%;
    height: 100%;
  }
  .sun-decoration {
    position: absolute;
    left: 0;
    top: 0;
    width: 150px;
    height: 140px;
    border-radius: 0 0 75px 0;
    background: radial-gradient(circle at 45px 42px, var(--sun-tone) 0 30px, rgba(242,122,126,0.55) 31px 70px, rgba(242,122,126,0) 71px);
  }
  .snow-decoration {
    position: absolute;
    left: 0;
    top: 0;
    width: 1200px;
    height: 693px;
    background: radial-gradient(ellipse at 75% 70%, rgba(120,140,190,0.22), rgba(120,140,190,0) 60%);
    clip-path: path("M1200,96 C1000,220 820,320 632,378 C420,440 200,500 0,551 L0,693 L1200,693 Z");
  }
  .brand {
    position: absolute;
    left: 400px;
    top: 44px;
    display: flex;
    align-items: center;
    gap: 28px;
  }
  .brand-mark {
    width: 128px;
    height: 128px;
    border-radius: 50%;
    background: var(--navy);
  }
  .brand-name {
    color: var(--navy);
    font-weight: 700;
    font-size: 54px;
    line-height: 1.08;
    text-transform: uppercase;
    letter-spacing: 1px;
  }
  .name-band {
    position: absolute;
    left: 0;
    top: 284px;
    width: 632px;
    height: 100px;
  }
  .name-band-top {
    position: absolute;
    left: 0; top: 0;
    width: 100%;
    height: 14px;
    background: var(--navy);
  }
  .name-band-main {
    position: absolute;
    left: 0; top: 14px;
    width: 100%;
    height: 86px;
    background: var(--red);
  }
  .name-band-rule {
    position: absolute;
    left: 0; top: 48px;
    width: 100%;
    height: 3px;
    background: var(--white);
  }
  .person-name {
    position: absolute;
    left: 20px;
    top: 11px;
    color: var(--white);
    font-size: 68px;
    line-height: 1;
    font-weight: 400;
    letter-spacing: 0.5px;
    text-transform: uppercase;
    white-space: nowrap;
    text-shadow: 3px 3px 2px rgba(0,0,0,0.75);
  }
  .contact-list {
    position: absolute;
    left: 550px;
    top: 442px;
    list-style: none;
    color: var(--white);
  }
  .contact-item {
    display: flex;
    align-items: center;
    height: 58px;
    margin-bottom: 14px;
    white-space: nowrap;
  }
  .contact-icon {
    width: 54px;
    height: 40px;
    margin-right: 24px;
    flex: none;
  }
  .contact-phone { font-size: 46px; }
  .contact-email, .contact-address { font-size: 35px; }
</style>
</head>
<body>
<main class="card">
  <svg class="card-backdrop" viewBox="0 0 1200 693" aria-hidden="true">
    <path d="M0,0 L338,0 C200,70 80,170 0,305 Z" fill="var(--red)"/>
    <path d="M1200,96 C1000,220 820,320 632,378 C420,440 200,500 0,551 L0,693 L1200,693 Z" fill="var(--navy)"/>
  </svg>

  <div class="sun-decoration" role="img" aria-label="Stylised sun symbolising heating"></div>
  <div class="snow-decoration" role="img" aria-label="Scattered snowflake pattern symbolising cooling"></div>

  <header class="brand">
    <span class="brand-mark"></span>
    <span class="brand-name">Brackwell HVAC<br>Service LLC</span>
  </header>

  <section class="name-band">
    <div class="name-band-top"></div>
    <div class="name-band-main"></div>
    <div class="name-band-rule"></div>
    <h1 class="person-name">Dale Vonnholt</h1>
  </section>

  <ul class="contact-list">
    <li class="contact-item contact-phone">
      <svg class="contact-icon" viewBox="0 0 54 40" aria-hidden="true">
        <path d="M2,14 C2,4 52,4 52,14 L52,18 L40,18 L40,12 C30,9 24,9 14,12 L14,18 L2,18 Z" fill="var(--white)"/>
        <path d="M12,20 L42,20 L48,38 L6,38 Z" fill="var(--white)"/>
        <circle cx="27" cy="29" r="5" fill="var(--navy)"/>
      </svg>
      (970) 555-0147
    </li>
    <li class="contact-item contact-email">
      <svg class="contact-icon" viewBox="0 0 54 40" aria-hidden="true">
        <rect x="3" y="6" width="48" height="30" fill="none" stroke="var(--white)" stroke-width="3"/>
        <path d="M3,6 L27,24 L51,6 M3,36 L21,20 M51,36 L33,20" fill="none" stroke="var(--white)" stroke-width="3"/>
      </svg>
      dale_brackwellhvac@inbox.net
    </li>
    <li class="contact-item contact-address">
      <svg class="contact-icon" viewBox="0 0 54 40" aria-hidden="true">
        <path d="M27,2 L4,22 L10,22 L10,39 L44,39 L44,22 L50,22 L40,13 L40,4 L35,4 L35,9 Z" fill="var(--white)"/>
        <rect x="22" y="26" width="10" height="13" fill="var(--navy)"/>
      </svg>
      P.O. Box 418 Brenvale, CO 80694
    </li>
  </ul>
</main>
</body>
</html>
```